E-Book-Cover für einen Kriminalroman
Zielgruppe
Ich veröffentliche meinen Roman “Die Schwelle” als E-Book.
Das Buch spielt in einer nahen Zukunft, in der die schwelle Nachrichten in die Vergangenheit möglich macht. Unfälle und Straftaten werden sofort ungeschehen gemacht. Jeder Bürger kann seinem vergangenen Ich eine Botschaft schicken - und so die eigene Geschichte “reparieren”. Auch Lukas, ein unscheinbarer Projektleiter, erhält eines Tag eine Nachricht aus der Zukunft: 'Halte dich von Merle fern. Sie wird dein Untergang sein'. Die Nachricht stellt Lukas vor ein Rätsel. Vor welcher Gefahr hat er sich gewarnt? Und wer ist Merle? Ein Jahr später wird Lukas durch Zufall Mitwisser einer politischen Verschwörung. Die Killer machen Jagd auf ihn und kennen jeden seiner nächsten Schritte. Die letzte Rettung ist ausgerechnet eine Frau namens Merle.
--- “Die Schwelle” spielt in der Zukunft, ist aber kein Science Fiction Roman. Die beschriebene Welt ist (außer der Zeitmanipulation) wie die unsere. Am ehesten ist das Buch also ein actionreicher Kriminalroman.
Die Hauptzielgruppe sind 25 - 45-jährige, zum Beispiel Leser von Jörg Wendlandt, Tobias Renwick oder Paul Fenmoor.
Aufgabenstellung
Gewünscht ist ein E-Book-Cover für die Verwendung auf Online-Plattformen wie Buchkai.
Autor: K.R. Anselm
Titel: Die Schwelle
Zusatz: Roman
Visuelle Anforderungen
Das Cover sollte eine Reihe von Türen zeigen. Begründung dazu: Im sogenannten Registerbüro muss der Protagonist in einer von vier nebeneinanderliegenden Türen treten und empfängt dort seine Nachricht aus der Zukunft. Das Thema “Entscheidungen fürs Leben” des Romans wird durch diese Türen visualisiert und als Symbol mehrmals aufgegriffen - dementsprechend ist es aus meiner Sicht perfekt für das Cover.
Für die Fotosuche: Das Registerbüro ist leicht heruntergekommen und wirkt kühl und unsympathisch. Dieses Bild https://de.bildquelle-beispiel.com/id/91730526 (auch noch einmal angehängt) zum Beispiel passt sehr gut.
Thema Hacking und Programmieren
Das Buch spielt in den Lebenswelten von Programmierern und Hackern; die schwelle ist eine Datenbank. Dies könnte durch Stil der Schrift oder anders unterstützt werden. Nur, wenn sinnvoll und ohne dass es wie ein Computerbuch aus den 90ern wirkt natürlich :)
- Die Font kann das Thema aufgreifen, aber bitte KEINE Vintage LED-Schrift im Stil von http://www.schriftlager-beispiel.com/lx-segment.font, sondern eine die einem modernen Monitor entspringt. Entweder verpixelt (Beispiel im Anhang) oder durch eine gepunktete Schrift in hoher "Auflösung" (Beispiel: http://www.schriftlager-beispiel.com/norbert-punkt.font, also nicht nur 7 Punkte in der Breite), hier könnte man die Ränder auch etwas blurren, um den Effekt eines Monitors zu erzielen
- Wenn der o.g. Schriftstil benutzt wird, bitte in Kleinbuchstaben (wie ein Befehl auf dem Terminal)
-> All kein Muss, nur wenn sinnvoll!
Weitere Anforderungen:
- Die Türen befinden sich in einem kühlen, sterilen BÜRO, dementsprechend dürfen sie nicht zu hübsch aussehen oder an Wohnzimmertüren erinnern
- Wenn Codezeilen als Hintergrundbestandteil genutzt..

```html
<!DOCTYPE html>
<html lang="de">
<head>
<meta charset="utf-8">
<title>Die Schwelle – K.R. Anselm</title>
<link rel="stylesheet" href="https://fonts.googleapis.com/css2?family=Barlow:wght@600&family=Doto:wght@700;900&display=swap">
<style>
  :root {
    --page: #ffffff;
    --wall-dark: #263634;
    --wall-mid: #3e5857;
    --wall-light: #56706f;
    --floor-dark: #5f625d;
    --floor-light: #8b8e88;
    --door-light: #dcdcd6;
    --door-shade: #b9bab4;
    --opening: #141a1a;
    --ink: #ffffff;
    --glow: rgba(255, 255, 255, 0.75);
  }
  html, body {
    margin: 0;
    padding: 0;
    width: 1200px;
    height: 1117px;
    overflow: hidden;
    background: var(--page);
  }
  .cover {
    position: absolute;
    left: 292px;
    top: 66px;
    width: 616px;
    height: 986px;
    overflow: hidden;
  }
  .cover-scene {
    position: absolute;
    inset: 0;
    background:
      linear-gradient(to bottom, transparent 0 83%, var(--floor-dark) 83%, var(--floor-light) 100%),
      radial-gradient(ellipse 70% 45% at 50% 40%, var(--wall-light), transparent 75%),
      linear-gradient(to bottom, var(--wall-dark) 0%, var(--wall-mid) 45%, var(--wall-mid) 83%);
  }
  .door-row {
    position: absolute;
    left: 0;
    top: 504px;
    width: 616px;
    height: 356px;
  }
  .door {
    position: absolute;
    top: 0;
    height: 316px;
    background: linear-gradient(to bottom, var(--door-light), var(--door-shade));
  }
  .door--cut { left: 0; width: 41px; }
  .door--second { left: 74px; width: 150px; }
  .door--open {
    left: 256px;
    width: 145px;
    background: linear-gradient(to right, var(--door-shade) 0 76%, var(--opening) 76% 100%);
  }
  .door--fourth { left: 433px; width: 149px; }
  .author,
  .genre {
    position: absolute;
    left: 0;
    width: 100%;
    text-align: center;
    color: var(--ink);
    font-family: "Barlow", sans-serif;
    font-weight: 600;
    font-size: 26px;
    line-height: 1;
    margin: 0;
  }
  .author { top: 66px; }
  .genre { top: 306px; letter-spacing: 0.5px; }
  .title {
    position: absolute;
    left: 0;
    top: 160px;
    width: 616px;
    height: 100px;
    overflow: visible;
  }
  .title text {
    font-family: "Doto", sans-serif;
    font-weight: 900;
    font-size: 98px;
    fill: var(--ink);
    filter: drop-shadow(0 0 3px var(--glow)) drop-shadow(0 0 8px var(--glow));
  }
</style>
</head>
<body>
  <main class="cover">
    <div class="cover-scene" role="img" aria-label="Foto: kahler, kühler Büroflur mit petrolfarbener Betonwand und grauem Betonboden"></div>
    <div class="door-row">
      <div class="door door--cut" role="img" aria-label="Foto: weiße Bürotür, vom Rand angeschnitten"></div>
      <div class="door door--second" role="img" aria-label="Foto: geschlossene weiße Bürotür"></div>
      <div class="door door--open" role="img" aria-label="Foto: halb geöffnete weiße Bürotür mit dunklem Spalt"></div>
      <div class="door door--fourth" role="img" aria-label="Foto: geschlossene weiße Bürotür"></div>
    </div>
    <p class="author">K.R. Anselm</p>
    <svg class="title" viewBox="0 0 616 100" aria-label="die schwelle">
      <text x="36" y="80" textLength="548" lengthAdjust="spacingAndGlyphs">die schwelle</text>
    </svg>
    <p class="genre">ROMAN</p>
  </main>
</body>
</html>
```